Webdesign/Updates

We would like a landing page for an online course for our educators. So a website with about 3 to 5 pages - Home, About US, Online course, blog, and Contact us. We have a wordpress site up using a template, but we are looking for something that connects more with our new logo.

Target Market(s)

Educators, workshop trainers/instructors, colleges, community schools, educational institutions, global organizations

Industry/Entity Type

Education

Contact Information for Business Card

Use the words below as place holders for the front:
Name
Title
Address line 1
Address line 2
Email
Phone
Website URL

--the back
Logo
1 short question, use "What do you 1234 about your program?"

Number of Pages Required

4 page

Requirements
Must have
• Home page
• Course Page
• Blog
• right side bar with social media content and invitation to subscribe to newsletter
• see logo colors in document
Nice to have
• Newsletter Page with graphic that can be on this page or page can be sent as a pdf via email or in an email.
Should not have
• Be better than attached description
• clean simple look but stylish

```html
<!DOCTYPE html>
<html lang="en">
<head>
<meta charset="utf-8">
<title>Bright Course Lab</title>
<link href="https://fonts.googleapis.com/css2?family=Lato:wght@400;700;900&family=Open+Sans:ital,wght@0,400;0,600;0,700;1,400&display=swap" rel="stylesheet">
<style>
:root{
  --blue:#2a90d3;
  --blue-dark:#1f7dbf;
  --green:#9cc42a;
  --red:#e6472a;
  --teal:#33b3c1;
  --ink:#1d1d1d;
  --body:#6a6a6a;
  --grey-bg:#f4f4f6;
  --footer:#1b1b1b;
  --white:#ffffff;
}
*{box-sizing:border-box;margin:0;padding:0}
html,body{width:1200px;height:3758px;overflow:hidden}
body{position:relative;font-family:"Open Sans",Arial,sans-serif;color:var(--body);background:var(--white)}
.abs{position:absolute}
.center{text-align:center;left:0;width:1200px}
h1,h2,h3{font-family:"Lato",Arial,sans-serif;color:var(--ink)}
.btn{position:absolute;display:flex;align-items:center;justify-content:center;background:var(--green);color:var(--white);font-family:"Lato",Arial,sans-serif;font-weight:700;font-size:18px;border-radius:30px;letter-spacing:.5px}

/* hero */
.hero{left:0;top:0;width:1200px;height:660px;background:linear-gradient(120deg,#6d5a4b 0%,#3e3531 35%,#8b7665 60%,#2f2a28 100%)}
.hero-shade{left:0;top:0;width:1200px;height:660px;background:rgba(0,0,0,.28)}
.brand{left:100px;top:20px;display:flex;align-items:center;gap:18px}
.brand-dot{width:58px;height:58px;border-radius:50%;background:var(--blue)}
.brand-name{font-family:"Lato",Arial,sans-serif;font-weight:700;font-size:29px;color:var(--white)}
.nav{right:110px;top:40px;display:flex;gap:26px;font-family:"Lato",Arial,sans-serif;font-weight:700;font-size:16px;color:var(--white)}
.nav .active{color:var(--green)}
.hero-title{top:140px;font-size:76px;font-weight:900;color:var(--white);letter-spacing:1px}
.hero-sub{top:240px;left:300px;width:600px;text-align:center;color:var(--white);font-size:18px;line-height:32px;font-weight:600}
.dots{top:578px;left:566px;display:flex;gap:4px}
.dots span{width:14px;height:14px;border-radius:50%;border:2px solid var(--white)}
.dots span.on{background:var(--white)}

/* program */
.sec-title{font-size:34px;font-weight:700}
.sec-sub{font-size:16px;color:var(--blue);font-weight:600}
.video{left:333px;top:858px;width:540px;height:356px;border:3px solid #e4e4e4;background:#fff;padding:6px}
.video-fill{width:100%;height:100%;background:linear-gradient(110deg,#3a4550 0%,#7a8a90 40%,#d8c9a6 70%,#f0d98c 100%);position:relative}
.play{position:absolute;left:236px;top:136px;width:60px;height:60px;border-radius:50%;background:#111}
.intro{left:205px;top:1246px;width:790px;text-align:center;font-size:14px;line-height:31px}

/* instructors */
.grey{left:0;top:1565px;width:1200px;height:660px;background:var(--grey-bg)}
.card{position:absolute;width:413px;height:170px;border:2px solid;background:var(--white);padding:22px 40px}
.card h3{font-size:19px;font-weight:700;margin-bottom:8px}
.card p{font-size:13px;line-height:22px}
.card .more{position:absolute;bottom:14px;font-family:"Lato",Arial,sans-serif;font-weight:900;font-size:13px}
.card.left{text-align:right;padding-right:110px}
.card.left .more{right:110px}
.card.right{text-align:left;padding-left:110px}
.card.right .more{left:110px}
.badge{position:absolute;width:130px;height:130px;border-radius:50%;display:flex;align-items:center;justify-content:center}

/* objectives */
.objectives{left:0;top:2225px;width:1200px;height:488px;background:linear-gradient(120deg,#3c3a3a 0%,#6b625c 40%,#504c4b 70%,#2c2b2c 100%)}
.obj-shade{left:0;top:2225px;width:1200px;height:488px;background:rgba(0,0,0,.45)}
.obj{position:absolute;top:2405px;width:321px;height:238px;border:2px solid var(--white);text-align:center;color:var(--white);padding-top:20px}
.obj h3{color:var(--white);font-size:23px;font-weight:700;margin:12px 0 16px}
.obj p{font-size:13px;line-height:22px;padding:0 30px}

/* testimonials */
.quotes{left:0;top:2713px;width:1200px;height:388px;background:linear-gradient(135deg,var(--blue) 0%,#2c98d8 50%,var(--blue-dark) 100%)}
.quote{position:absolute;top:2843px;width:330px;color:var(--white)}
.avatar{position:absolute;left:0;top:0;width:78px;height:78px;border-radius:50%;background:#dfe7ee;border:3px solid var(--white)}
.quote .text{position:absolute;left:92px;top:0;width:238px;font-style:italic;font-size:11.5px;line-height:19px}
.quote .who{position:absolute;left:92px;top:94px;font-size:11px;font-weight:700;text-transform:uppercase}
.quote .role{position:absolute;left:92px;top:112px;font-size:10px;font-style:italic}
.quote .stars{position:absolute;left:92px;top:148px;display:flex;gap:4px}
.arrow{position:absolute;top:2905px;width:36px;height:36px;border-radius:50%;border:2px solid var(--white);display:flex;align-items:center;justify-content:center}

/* join */
.field{position:absolute;height:45px;border:1px solid #bdbdbd;font-size:14px;color:#444;padding:13px 14px}

/* footer */
.footer{left:0;top:3550px;width:1200px;height:208px;background:var(--footer)}
.social{position:absolute;top:3520px;width:60px;height:60px;border-radius:50%;background:var(--blue);border:3px solid var(--white);display:flex;align-items:center;justify-content:center}
.foot-line{color:var(--white);font-size:14px;text-align:center;left:0;width:1200px}
.foot-small{font-size:13px}
</style>
</head>
<body>

<!-- hero -->
<div class="abs hero" role="img" aria-label="Photo of a group of learners working together around a table"></div>
<div class="abs hero-shade"></div>
<div class="abs brand"><span class="brand-dot"></span><span class="brand-name">Bright Course Lab</span></div>
<nav class="abs nav"><span class="active">Home</span><span>Course</span><span>Blog</span><span>Consulting</span><span>About Me</span>
  <svg width="16" height="16" viewBox="0 0 16 16"><circle cx="6.5" cy="6.5" r="5" fill="none" stroke="#fff" stroke-width="2"/><line x1="10" y1="10" x2="15" y2="15" stroke="#fff" stroke-width="2.4"/></svg>
</nav>
<h1 class="abs center hero-title">BRIGHT COURSE LAB</h1>
<p class="abs hero-sub">Get comfortable, confident and satisfied teaching online with the ultimate course design program. A comprehensive program for building accredited online courses.</p>
<div class="btn" style="left:502px;top:370px;width:196px;height:56px">GET STARTED</div>
<div class="abs dots"><span class="on"></span><span></span><span></span><span></span></div>

<!-- program -->
<h2 class="abs center sec-title" style="top:728px">The Ultimate Course Design Program</h2>
<p class="abs center sec-sub" style="top:790px">A Practical, Comprehensive Approach that Gets you Ahead</p>
<div class="abs video"><div class="video-fill" role="img" aria-label="Video still of two colleagues planning with sticky notes on a wall"><span class="play"><svg width="60" height="60" viewBox="0 0 60 60"><path d="M24 18 L42 30 L24 42 Z" fill="#fff"/></svg></span></div></div>
<p class="abs intro">The Ultimate Course Design Program will teach you an organized and practical approach to creating accredit-able courses that are visually appealing, engaging and highly interactive. Through this virtual program with LIVE weekly meetings and virtual one-on-one meetings, you will become more comfortable and satisfied with what you design, how you create it, and best of all, how you teach.</p>
<div class="btn" style="left:502px;top:1405px;width:196px;height:58px">GET STARTED</div>

<!-- instructors -->
<div class="abs grey"></div>
<h2 class="abs center sec-title" style="top:1620px">Meet our Experienced and Enthusiastic Instructors</h2>
<p class="abs center sec-sub" style="top:1682px">A Collaborative Approach to Creating Accreditable Online Courses</p>

<div class="card left" style="left:100px;top:1766px;border-color:var(--blue)">
  <h3>Effective Lessons</h3>
  <p>At vero eos et accusamus et iusto odiodign issimos ducimus qui blanditiis prae sentiu mvoluptatum deleniti atque.</p>
  <span class="more" style="color:var(--blue)">READ MORE</span>
</div>
<div class="badge" style="left:448px;top:1785px;background:var(--blue)">
  <svg width="56" height="56" viewBox="0 0 56 56"><path d="M14 8 H44 V42 H18 a4 4 0 0 0 0 8 H44" fill="none" stroke="#fff" stroke-width="4" stroke-linejoin="round"/><path d="M14 8 V46" stroke="#fff" stroke-width="4"/><line x1="22" y1="18" x2="38" y2="18" stroke="#fff" stroke-width="3"/><line x1="22" y1="26" x2="38" y2="26" stroke="#fff" stroke-width="3"/></svg>
</div>

<div class="card right" style="left:689px;top:1766px;border-color:var(--red)">
  <h3>Save time &amp; money</h3>
  <p>At vero eos et accusamus et iusto odiodign issimos ducimus qui blanditiis prae sentiu mvoluptatum deleniti atque.</p>
  <span class="more" style="color:var(--red)">READ MORE</span>
</div>
<div class="badge" style="left:624px;top:1785px;background:var(--red)">
  <svg width="56" height="56" viewBox="0 0 56 56"><circle cx="28" cy="28" r="21" fill="none" stroke="#fff" stroke-width="4"/><path d="M28 15 V28 H38" fill="none" stroke="#fff" stroke-width="4" stroke-linecap="round"/></svg>
</div>

<div class="card left" style="left:100px;top:1971px;border-color:var(--green)">
  <h3>Course Excellence</h3>
  <p>At vero eos et accusamus et iusto odiodign issimos ducimus qui blanditiis prae sentiu mvoluptatum deleniti atque.</p>
  <span class="more" style="color:var(--green)">READ MORE</span>
</div>
<div class="badge" style="left:448px;top:1990px;background:var(--green)">
  <svg width="56" height="56" viewBox="0 0 56 56"><rect x="8" y="24" width="10" height="22" rx="2" fill="#fff"/><path d="M21 24 L30 8 c4 0 6 3 5 7 l-2 7 h12 c3 0 5 3 4 6 l-4 15 c-1 2 -3 3 -5 3 H21 Z" fill="#fff"/></svg>
</div>

<div class="card right" style="left:689px;top:1971px;border-color:var(--teal)">
  <h3>Experienced Instructors</h3>
  <p>At vero eos et accusamus et iusto odiodign issimos ducimus qui blanditiis prae sentiu mvoluptatum deleniti atque.</p>
  <span class="more" style="color:var(--teal)">READ MORE</span>
</div>
<div class="badge" style="left:624px;top:1990px;background:var(--teal)">
  <svg width="60" height="56" viewBox="0 0 60 56"><circle cx="30" cy="16" r="8" fill="#fff"/><path d="M16 44 c0-10 6-16 14-16 s14 6 14 16 Z" fill="#fff"/><circle cx="12" cy="22" r="6" fill="#fff"/><path d="M2 44 c0-8 4-12 10-12 c2 0 3 0 4 1 c-3 3 -4 7 -4 11 Z" fill="#fff"/><circle cx="48" cy="22" r="6" fill="#fff"/><path d="M58 44 c0-8 -4-12 -10-12 c-2 0 -3 0 -4 1 c3 3 4 7 4 11 Z" fill="#fff"/></svg>
</div>

<!-- objectives -->
<div class="abs objectives" role="img" aria-label="Photo of hands working at a desk with a notebook"></div>
<div class="abs obj-shade"></div>
<h2 class="abs center sec-title" style="top:2278px;color:var(--white)">Learning Objectives</h2>
<p class="abs center" style="top:2340px;color:var(--white);font-size:16px;font-weight:600">So many academic goals that we expect you to achieve</p>

<div class="obj" style="left:100px">
  <svg width="44" height="52" viewBox="0 0 44 52"><path d="M22 3 a16 16 0 0 0 -9 29 v7 h18 v-7 a16 16 0 0 0 -9 -29 Z" fill="none" stroke="#fff" stroke-width="3.5"/><line x1="15" y1="45" x2="29" y2="45" stroke="#fff" stroke-width="3.5"/></svg>
  <h3>Skills</h3>
  <p>Nam libero tempore, cum soluta nobis est eligendi optio cumque nihil impedi quo minus id quod maxime placeat</p>
</div>
<div class="obj" style="left:441px">
  <svg width="44" height="52" viewBox="0 0 44 52"><circle cx="22" cy="13" r="11" fill="#fff"/><path d="M3 50 c0-14 8-22 19-22 s19 8 19 22 Z" fill="#fff"/></svg>
  <h3>Self Learning</h3>
  <p>Nam libero tempore, cum soluta nobis est eligendi optio cumque nihil impedi quo minus id quod maxime placeat</p>
</div>
<div class="obj" style="left:782px">
  <svg width="44" height="52" viewBox="0 0 44 52"><path d="M10 4 H40 V38 H14 a4 4 0 0 0 0 8 H40" fill="none" stroke="#fff" stroke-width="3.5" stroke-linejoin="round"/><path d="M10 4 V42" stroke="#fff" stroke-width="3.5"/><line x1="18" y1="14" x2="33" y2="14" stroke="#fff" stroke-width="3"/><line x1="18" y1="22" x2="33" y2="22" stroke="#fff" stroke-width="3"/></svg>
  <h3>Knowledge</h3>
  <p>Nam libero tempore, cum soluta nobis est eligendi optio cumque nihil impedi quo minus id quod maxime placeat</p>
</div>

<!-- testimonials -->
<div class="abs quotes"></div>
<h2 class="abs center sec-title" style="top:2762px;color:var(--white)">What People are Saying</h2>
<div class="arrow" style="left:28px"><svg width="14" height="14" viewBox="0 0 14 14"><path d="M9 2 L4 7 L9 12" fill="none" stroke="#fff" stroke-width="2"/></svg></div>
<div class="arrow" style="left:1134px"><svg width="14" height="14" viewBox="0 0 14 14"><path d="M5 2 L10 7 L5 12" fill="none" stroke="#fff" stroke-width="2"/></svg></div>

<div class="quote" style="left:100px">
  <span class="avatar"></span>
  <p class="text">&ldquo; At vero eos et accusamus et iustodio dignissimos ducimus qui blanditiispraesnt ium voluptatum deleniti atq.</p>
  <span class="who">Dana Whitfield</span><span class="role">Financial Services Professional</span>
  <div class="stars"><svg width="96" height="18" viewBox="0 0 96 18"><g fill="#c8dc3c"><path id="st" d="M9 1 L11.3 6.5 L17 7 L12.6 10.8 L14 16.5 L9 13.4 L4 16.5 L5.4 10.8 L1 7 L6.7 6.5 Z"/><use href="#st" x="19"/><use href="#st" x="38"/><use href="#st" x="57"/></g><use href="#st" x="76" fill="none" stroke="#c8dc3c" stroke-width="1.3"/></svg></div>
</div>
<div class="quote" style="left:442px">
  <span class="avatar"></span>
  <p class="text">&ldquo; At vero eos et accusamus et iustodio dignissimos ducimus qui blanditiispraesnt ium voluptatum deleniti atque.</p>
  <span class="who">Marisol T. Vega</span><span class="role">National Urban Fellow at the Houston</span>
  <div class="stars"><svg width="96" height="18" viewBox="0 0 96 18"><g fill="#c8dc3c"><use href="#st"/><use href="#st" x="19"/><use href="#st" x="38"/><use href="#st" x="57"/></g><use href="#st" x="76" fill="none" stroke="#c8dc3c" stroke-width="1.3"/><path d="M85 1 L85 13.4 L80 16.5 L81.4 10.8 L77 7 L82.7 6.5 Z" fill="#c8dc3c"/></svg></div>
</div>
<div class="quote" style="left:790px">
  <span class="avatar"></span>
  <p class="text">&ldquo; At vero eos et accusamus et iustodio dignissimos ducimus qui blanditiispraesnt ium voluptatum deleniti atque.</p>
  <span class="who">Ruth Calloway</span><span class="role">Creative Strategist | Entrepreneur &amp; Upcoming</span>
  <div class="stars"><svg width="96" height="18" viewBox="0 0 96 18"><g fill="#c8dc3c"><use href="#st"/><use href="#st" x="19"/><use href="#st" x="38"/><use href="#st" x="57"/></g><use href="#st" x="76" fill="none" stroke="#c8dc3c" stroke-width="1.3"/></svg></div>
</div>

<!-- join -->
<h2 class="abs center sec-title" style="top:3172px">Join our Community</h2>
<div class="field" style="left:253px;top:3249px;width:342px">Name:</div>
<div class="field" style="left:606px;top:3249px;width:342px">Email:</div>
<div class="field" style="left:253px;top:3309px;width:695px">Phone:</div>
<div class="btn" style="left:506px;top:3387px;width:192px;height:57px">GET IT NOW!</div>

<!-- footer -->
<div class="abs footer"></div>
<span class="social" style="left:465px"></span>
<span class="social" style="left:535px"></span>
<span class="social" style="left:605px"></span>
<span class="social" style="left:675px"><svg width="24" height="18" viewBox="0 0 24 18"><rect x="1" y="1" width="22" height="16" rx="2" fill="#fff"/><path d="M2 2 L12 10 L22 2" fill="none" stroke="#2a90d3" stroke-width="2"/></svg></span>
<p class="abs foot-line" style="top:3614px">
  <svg width="12" height="16" viewBox="0 0 12 16"><path d="M6 0 a6 6 0 0 0 -6 6 c0 4 6 10 6 10 s6-6 6-10 a6 6 0 0 0 -6 -6 Z" fill="#fff"/><circle cx="6" cy="6" r="2.2" fill="#1b1b1b"/></svg>
  Nam libero tempor&nbsp; soluta nobis est &nbsp;&nbsp;|&nbsp;&nbsp;
  <svg width="14" height="14" viewBox="0 0 14 14"><path d="M3 0 L6 4 L4.5 6 C5.5 8 6 8.5 8 9.5 L10 8 L14 11 L12 14 C6 14 0 8 0 2 Z" fill="#fff"/></svg>
  1 888 888 8888 &nbsp;&nbsp;|&nbsp;&nbsp;
  <svg width="16" height="12" viewBox="0 0 16 12"><rect width="16" height="12" rx="1.5" fill="#fff"/><path d="M1 1 L8 7 L15 1" fill="none" stroke="#1b1b1b" stroke-width="1.5"/></svg>
  info@brightcourselab.com
</p>
<p class="abs foot-line foot-small" style="top:3655px">Help &nbsp;|&nbsp; FAQ &nbsp;|&nbsp; Support &nbsp;|&nbsp; Sitemap &nbsp;|&nbsp; Terms Of Use &nbsp;|&nbsp; Privacy Statement</p>
<p class="abs foot-line foot-small" style="top:3690px">Copyrights © 2018, Bright Course Lab. All rights reserved.</p>

</body>
</html>
```